Design Challege - Simplify a Complex Message

We have a new website design, but one of the pages presents a particular problem.

Our company does ERP implementations. We have developed a proprietary approach to these implementations based on the idea that you must get eight (and only eight) things right. These eight things are listed below, summarized in one or two words each:

1. Value
2. Capability
3. Functionality
4. Data
5. Technology
6. Change Leadership
7. Quality
8. Governance

Each of these eight things can be summarized in a short paragraph, but when you combine all eight summaries with a brief introductory text, the result is a lot of text - so much text that the casual surfer may be overwhelmed by it.

The winning design will find an engaging way to present the information in a way that presents a high-level summary, using icons and one- or two-word descriptions above but revealing more information when clicked.

Our current design for this information, with a paragraph describing the eight elements in a table, is included as an upload in PDF and Microsoft Word formats. We are looking for a creative way to display these eight things, showing the detail only when the user wants to see it.

The website is being built in WordPress, using Elementor as a page builder.

We will implement (code) the page, but the winner will be asked to specify the widget or other add-in if one is required.

The design does not need to include a header or footer, we have those.

Target Market(s)

Business executives working in technology

Industry/Entity Type

Any

Number of Pages Required

1 page

Font styles to use
Sans Serif

Requirements
Must have
• A design for the body of the page, but not the header or footer.
Nice to have
• Unique icons or images appropriate for each of the eight things.
Should not have
• A lot of text on one page

```html
<!DOCTYPE html>
<html lang="en">
<head>
<meta charset="utf-8">
<title>ERP Implementations – Eight Things to Get Right</title>
<link href="https://fonts.googleapis.com/css2?family=Montserrat:wght@400;500;600;700&display=swap" rel="stylesheet">
<style>
  :root{
    --page-bg:#f5f5f9;
    --brand-blue:#2a86c8;
    --tile-dark:#1b78b8;
    --tile-light:#2a8ccb;
    --tile-active:#1570ad;
    --ink:#3c3c46;
    --ink-soft:#4a4a55;
    --label-grey:#7d7d86;
    --white:#ffffff;
  }
  *{box-sizing:border-box;margin:0;padding:0}
  html,body{width:1200px;height:1133px;overflow:hidden}
  body{background:var(--page-bg);font-family:"Montserrat",Arial,sans-serif;position:relative;color:var(--ink)}

  .intro{position:absolute;left:0;top:0;width:1200px;height:210px;text-align:center}
  .intro__title{position:absolute;left:50%;top:52px;transform:translateX(-50%);white-space:nowrap;font-size:18px;font-weight:600;color:var(--brand-blue);letter-spacing:.2px;line-height:22px;border-bottom:1.5px solid var(--brand-blue);padding-bottom:4px}
  .intro__subtitle{position:absolute;left:0;width:1200px;top:99px;font-size:13px;font-weight:600;color:var(--ink);line-height:17px}
  .intro__text{position:absolute;left:380px;width:440px;font-size:8.9px;line-height:13.75px;color:var(--ink-soft);white-space:nowrap}
  .intro__text--first{top:129px}
  .intro__text--second{top:170px}

  .view-label{position:absolute;font-size:12.5px;font-weight:600;color:var(--label-grey);letter-spacing:.2px}
  .view-label--normal{left:41px;top:396px}
  .view-label--hover{left:32px;top:873px}

  .pillars{position:absolute;left:231px;width:738px;height:369px;display:grid;grid-template-columns:repeat(4,1fr);grid-template-rows:repeat(2,1fr);box-shadow:0 6px 16px rgba(30,60,100,.12)}
  .pillars--normal{top:221px}
  .pillars--hover{top:696px}

  .pillar{display:flex;flex-direction:column;align-items:center;text-align:center;padding-top:29px;color:var(--white)}
  .pillar--dark{background:var(--tile-dark)}
  .pillar--light{background:var(--tile-light)}
  .pillar__icon{width:42px;height:42px}
  .pillar__name{margin-top:20px;font-size:10.6px;font-weight:700;line-height:13px;letter-spacing:.1px;white-space:nowrap}
  .pillar__summary{margin-top:7px;font-size:9px;line-height:15px;font-weight:400;white-space:nowrap}
  .pillar__link{margin-top:9px;font-size:9px;font-weight:700;line-height:12px}

  .pillar--open{grid-column:span 2;background:var(--tile-active);position:relative;display:block;padding:0}
  .pillar--open .pillar__icon{position:absolute;left:37px;top:35px}
  .pillar--open .pillar__name{position:absolute;left:24px;width:68px;top:91px;margin:0;text-align:center}
  .pillar__detail{position:absolute;left:115px;top:38px;text-align:left;font-size:9px;line-height:15px;letter-spacing:.25px;white-space:nowrap}

  .cursor{position:absolute;left:535px;top:843px;width:32px;height:48px}
  .icon-sprites{position:absolute;width:0;height:0;overflow:hidden}
</style>
</head>
<body>

<svg class="icon-sprites" aria-hidden="true">
  <defs>
    <symbol id="icon-value" viewBox="0 0 40 40" fill="none" stroke="#fff" stroke-width="1.4" stroke-linecap="round" stroke-linejoin="round">
      <circle cx="20" cy="24" r="6.5"/><circle cx="20" cy="24" r="4.5"/>
      <path d="M21.5 21.5h-2.2a1.2 1.2 0 0 0 0 2.5h1.4a1.2 1.2 0 0 1 0 2.5h-2.3M20 20.5v7"/>
      <path d="M20 16V6M17 9l3-3 3 3M8 26V18M5.5 20.5 8 18l2.5 2.5M32 26V18M29.5 20.5 32 18l2.5 2.5"/>
      <path d="M6 29v2M10 29v2M30 29v2M34 29v2"/>
    </symbol>
    <symbol id="icon-capability" viewBox="0 0 40 40" fill="none" stroke="#fff" stroke-width="1.3" stroke-linecap="round" stroke-linejoin="round">
      <circle cx="20" cy="20" r="3"/><path d="M15 33v-5a5 5 0 0 1 10 0v5M18 25l2 4 2-4"/>
      <circle cx="20" cy="8" r="2.5"/><path d="M20 3v1.5M15.5 8H14M26 8h-1.5"/>
      <circle cx="30" cy="13" r="2.5"/><circle cx="30" cy="13" r="4" stroke-dasharray="2 1.5"/>
      <path d="M8 13a14 14 0 0 1 4-5M7 22v-4M5 20l2-2 2 2M30 26l1 2 2 .3-1.5 1.4.4 2-1.9-1-1.9 1 .4-2-1.5-1.4 2-.3z"/>
      <path d="M10 30a14 14 0 0 1-2-4" stroke-dasharray="1.5 1.5"/>
    </symbol>
    <symbol id="icon-functionality" viewBox="0 0 40 40" fill="none" stroke="#fff" stroke-width="1.4">
      <circle cx="22" cy="9" r="3"/><circle cx="22" cy="9" r="6" stroke-dasharray="3 1.5"/>
      <circle cx="11" cy="22" r="3"/><circle cx="11" cy="22" r="6.5" stroke-dasharray="3 1.5"/>
      <circle cx="28" cy="27" r="3"/><circle cx="28" cy="27" r="6.5" stroke-dasharray="3 1.5"/>
    </symbol>
    <symbol id="icon-data" viewBox="0 0 40 40" fill="none" stroke="#fff" stroke-width="1.4" stroke-linecap="round" stroke-linejoin="round">
      <path d="M10 25a6 6 0 0 1 0-12 9 9 0 0 1 17-2 7 7 0 0 1 3 14"/>
      <path d="M20 13v15M14 18v6l-2 2v2M26 18v6l2 2v2"/>
      <circle cx="20" cy="30" r="2"/><circle cx="12" cy="30" r="2"/><circle cx="28" cy="30" r="2"/>
    </symbol>
    <symbol id="icon-technology" viewBox="0 0 40 40" fill="none" stroke="#fff" stroke-width="1.4" stroke-linecap="round" stroke-linejoin="round">
      <rect x="5" y="5" width="30" height="30"/><rect x="8" y="8" width="24" height="24"/>
      <circle cx="14" cy="14" r="2.5"/><circle cx="26" cy="14" r="2.5"/><circle cx="14" cy="26" r="2.5"/><circle cx="26" cy="26" r="2.5"/>
      <path d="M16 16l8 8M24 16l-8 8M28.5 28.5 35 35"/>
    </symbol>
    <symbol id="icon-change" viewBox="0 0 40 40" fill="none" stroke="#fff" stroke-width="1.4" stroke-linecap="round">
      <circle cx="20" cy="14" r="3.5"/><path d="M14 26a6 6 0 0 1 12 0"/>
      <circle cx="9" cy="20" r="3"/><path d="M3 31a6 6 0 0 1 12 0"/>
      <circle cx="31" cy="20" r="3"/><path d="M25 31a6 6 0 0 1 12 0"/>
      <path d="M20 4v3M12 7l2 2M28 7l-2 2M8 12h2M30 12h2"/>
    </symbol>
    <symbol id="icon-quality" viewBox="0 0 40 40" fill="none" stroke="#fff" stroke-width="1.4" stroke-linecap="round" stroke-linejoin="round">
      <path d="M20 3l3 2.5 4-.5 1 3.8 3.5 2-1.4 3.7 1.4 3.7-3.5 2-1 3.8-4-.5L20 26l-3-2.5-4 .5-1-3.8-3.5-2 1.4-3.7L8.5 11l3.5-2 1-3.8 4 .5z"/>
      <path d="M15.5 14.5l3 3 6-6"/>
      <path d="M13 24l-3 10 4-2 2 4 3-9M27 24l3 10-4-2-2 4-3-9"/>
    </symbol>
    <symbol id="icon-governance" viewBox="0 0 40 40" fill="none" stroke="#fff" stroke-width="1.4" stroke-linecap="round" stroke-linejoin="round">
      <circle cx="20" cy="6" r="2.5"/><path d="M16 13a4 4 0 0 1 8 0"/>
      <path d="M8 16v-4h6M32 16v-4h-6"/>
      <circle cx="8" cy="22" r="2.5"/><path d="M3 34v-3a5 5 0 0 1 10 0v3z"/>
      <circle cx="20" cy="22" r="2.5"/><path d="M15 34v-3a5 5 0 0 1 10 0v3z"/>
      <circle cx="32" cy="22" r="2.5"/><path d="M27 34v-3a5 5 0 0 1 10 0v3z"/>
    </symbol>
  </defs>
</svg>

<header class="intro">
  <h1 class="intro__title">ERP IMPLEMENTATIONS</h1>
  <h2 class="intro__subtitle">Eight Things to Get Right</h2>
  <p class="intro__text intro__text--first">Like the roots and branches of a tree, there are many considerations in an ERP<br>implementation. Focus too much on the minor details, and you can lose sight of the tree.</p>
  <p class="intro__text intro__text--second">In an ERP implementation, you must get eight major things right to be successful. Ignore<br>any of them, and your implementation will fail. Get them right, and you will likely succeed.</p>
</header>

<p class="view-label view-label--normal">(NORMAL VIEW)</p>

<section class="pillars pillars--normal">
  <article class="pillar pillar--dark"><svg class="pillar__icon"><use href="#icon-value"/></svg><h3 class="pillar__name">VALUE</h3><p class="pillar__summary">High-value, aligned, and<br>resource-efficient project</p><span class="pillar__link">Learn More</span></article>
  <article class="pillar pillar--light"><svg class="pillar__icon"><use href="#icon-capability"/></svg><h3 class="pillar__name">CAPABILITY</h3><p class="pillar__summary">A capable team implementing<br>the project on their own</p><span class="pillar__link">Learn More</span></article>
  <article class="pillar pillar--dark"><svg class="pillar__icon"><use href="#icon-functionality"/></svg><h3 class="pillar__name">FUNCTIONALITY</h3><p class="pillar__summary">ERP supports current<br>and future projects</p><span class="pillar__link">Learn More</span></article>
  <article class="pillar pillar--light"><svg class="pillar__icon"><use href="#icon-data"/></svg><h3 class="pillar__name">DATA</h3><p class="pillar__summary">Insights require careful<br>data management</p><span class="pillar__link">Learn More</span></article>
  <article class="pillar pillar--light"><svg class="pillar__icon"><use href="#icon-technology"/></svg><h3 class="pillar__name">TECHNOLOGY</h3><p class="pillar__summary">Consider integration and<br>scalability of your system</p><span class="pillar__link">Learn More</span></article>
  <article class="pillar pillar--dark"><svg class="pillar__icon"><use href="#icon-change"/></svg><h3 class="pillar__name">CHANGE LEADERSHIP</h3><p class="pillar__summary">Focus on human aspects in ERP<br>implementation for success</p><span class="pillar__link">Learn More</span></article>
  <article class="pillar pillar--light"><svg class="pillar__icon"><use href="#icon-quality"/></svg><h3 class="pillar__name">QUALITY</h3><p class="pillar__summary">Take an approach to quality<br>beginning with perceptions</p><span class="pillar__link">Learn More</span></article>
  <article class="pillar pillar--dark"><svg class="pillar__icon"><use href="#icon-governance"/></svg><h3 class="pillar__name">GOVERNANCE</h3><p class="pillar__summary">Without both mangement &amp;<br>leadership, the best projects fail</p><span class="pillar__link">Learn More</span></article>
</section>

<p class="view-label view-label--hover">(HOVER VIEW)</p>

<section class="pillars pillars--hover">
  <article class="pillar pillar--open">
    <svg class="pillar__icon"><use href="#icon-value"/></svg>
    <h3 class="pillar__name">VALUE</h3>
    <p class="pillar__detail">The project must provide value that significantly<br>exceeds potential project costs and should be<br>aligned with the company's strategy. Its value<br>and strategic alignment must be part of a vision<br>shared by the company's leadership. Value<br>from the project must be delivered in a way<br>that respects resource constraints.</p>
  </article>
  <article class="pillar pillar--dark"><svg class="pillar__icon"><use href="#icon-functionality"/></svg><h3 class="pillar__name">FUNCTIONALITY</h3><p class="pillar__summary">ERP supports current<br>and future projects</p><span class="pillar__link">Learn More</span></article>
  <article class="pillar pillar--light"><svg class="pillar__icon"><use href="#icon-data"/></svg><h3 class="pillar__name">DATA</h3><p class="pillar__summary">Insights require careful<br>data management</p><span class="pillar__link">Learn More</span></article>
  <article class="pillar pillar--light"><svg class="pillar__icon"><use href="#icon-technology"/></svg><h3 class="pillar__name">TECHNOLOGY</h3><p class="pillar__summary">Consider integration and<br>scalability of your system</p><span class="pillar__link">Learn More</span></article>
  <article class="pillar pillar--dark"><svg class="pillar__icon"><use href="#icon-change"/></svg><h3 class="pillar__name">CHANGE LEADERSHIP</h3><p class="pillar__summary">Focus on human aspects in ERP<br>implementation for success</p><span class="pillar__link">Learn More</span></article>
  <article class="pillar pillar--light"><svg class="pillar__icon"><use href="#icon-quality"/></svg><h3 class="pillar__name">QUALITY</h3><p class="pillar__summary">Take an approach to quality<br>beginning with perceptions</p><span class="pillar__link">Learn More</span></article>
  <article class="pillar pillar--dark"><svg class="pillar__icon"><use href="#icon-governance"/></svg><h3 class="pillar__name">GOVERNANCE</h3><p class="pillar__summary">Without both mangement &amp;<br>leadership, the best projects fail</p><span class="pillar__link">Learn More</span></article>
</section>

<svg class="cursor" viewBox="0 0 32 48" aria-hidden="true">
  <path d="M1 1v34l8-8 7 15 6-3-7-14h12z" fill="#000" stroke="#fff" stroke-width="1.5" stroke-linejoin="round"/>
</svg>

</body>
</html>
```